Peach Point of Sale Cards for Grocery Retail Markets

We are looking to update our peach point of sale card and price card. The cards will need to be 7" x 11" with a .125 bleed - one sided. See attached for the old versions. We would like this to use photos that look like true Washington State Peaches. Here are the bullet points we would like to use: - New Crop!- Tree Ripened- Excellent FlavorNOTE: The price card just needs to have a space where a retailer can write in the sale price of the item. See attachment with the white box.

Target Market(s)

Retail market shoppers

Requirements
Must have
• Pictures of Peaches Only

```html
<!DOCTYPE html>
<html lang="en">
<head>
<meta charset="utf-8">
<title>Peach Point of Sale Card</title>
<link rel="stylesheet" href="https://fonts.googleapis.com/css2?family=Archivo+Black&family=Dancing+Script:wght@700&family=Kaushan+Script&display=swap">
<style>
  :root {
    --backdrop: #e6e2a0;
    --peach-red: #d9442f;
    --peach-orange: #ee8a3a;
    --peach-gold: #f3b35a;
    --peach-deep: #b8321f;
    --ribbon-light: #a6d93a;
    --ribbon-mid: #6cbf2a;
    --ribbon-dark: #3f8f1c;
    --ribbon-fold: #2e6d14;
    --brand-green: #1f7a35;
    --text-white: #ffffff;
    --text-outline: #c9531f;
    --price-ink: #111111;
    --price-panel: #ffffff;
  }
  * { margin: 0; padding: 0; box-sizing: border-box; }
  html, body {
    width: 1200px;
    height: 800px;
    overflow: hidden;
    background: var(--backdrop);
  }
  .pos-card {
    position: absolute;
    left: 50px;
    top: 32px;
    width: 1100px;
    height: 736px;
    overflow: hidden;
    box-shadow: 0 6px 18px rgba(0,0,0,0.18);
  }
  .peach-photo {
    position: absolute;
    inset: 0;
    background:
      radial-gradient(circle at 22% 30%, var(--peach-red) 0%, transparent 38%),
      radial-gradient(circle at 55% 55%, var(--peach-orange) 0%, transparent 40%),
      radial-gradient(circle at 85% 25%, var(--peach-gold) 0%, transparent 35%),
      radial-gradient(circle at 40% 90%, var(--peach-deep) 0%, transparent 40%),
      linear-gradient(135deg, var(--peach-red), var(--peach-orange) 55%, var(--peach-red));
  }
  .card-graphics {
    position: absolute;
    inset: 0;
  }
  .product-title {
    position: absolute;
    left: 135px;
    top: 52px;
    width: 848px;
    height: 96px;
    display: flex;
    align-items: center;
    justify-content: center;
    font-family: "Dancing Script", cursive;
    font-weight: 700;
    font-size: 66px;
    color: var(--text-white);
    text-shadow: 3px 3px 0 var(--ribbon-fold);
  }
  .headline {
    position: absolute;
    left: 105px;
    top: 292px;
    font-family: "Archivo Black", sans-serif;
    font-size: 74px;
    color: var(--text-white);
    -webkit-text-stroke: 2px var(--text-outline);
    text-shadow: 4px 4px 0 var(--text-outline);
    letter-spacing: 1px;
  }
  .benefit-list {
    position: absolute;
    left: 104px;
    top: 410px;
    list-style: none;
  }
  .benefit {
    display: flex;
    align-items: center;
    height: 64px;
    font-family: "Archivo Black", sans-serif;
    font-size: 42px;
    color: var(--text-white);
    text-shadow: 3px 3px 0 var(--text-outline);
  }
  .benefit svg { margin-right: 18px; flex: none; }
  .brand {
    position: absolute;
    left: 58px;
    top: 573px;
    display: flex;
    align-items: center;
  }
  .brand-dot {
    width: 128px;
    height: 128px;
    border-radius: 50%;
    background: var(--peach-gold);
    flex: none;
  }
  .brand-name {
    margin-left: 28px;
    font-family: "Archivo Black", sans-serif;
    font-size: 31px;
    line-height: 1.1;
    color: var(--brand-green);
  }
  .price {
    position: absolute;
    right: 50px;
    top: 505px;
    text-align: center;
    color: var(--price-ink);
    font-family: "Kaushan Script", cursive;
  }
  .price-amount { font-size: 96px; line-height: 1; }
  .price-amount sup { font-size: 52px; vertical-align: 36px; }
  .price-unit { font-size: 48px; line-height: 1; margin-top: -6px; }
</style>
</head>
<body>
  <main class="pos-card">
    <div class="peach-photo" role="img" aria-label="Close-up photograph of ripe red and orange peaches filling the card"></div>

    <svg class="card-graphics" width="1100" height="736" viewBox="0 0 1100 736" aria-hidden="true">
      <defs>
        <linearGradient id="ribbon-face" x1="0" y1="0" x2="1" y2="0">
          <stop offset="0" stop-color="var(--ribbon-mid)"/>
          <stop offset="0.5" stop-color="var(--ribbon-light)"/>
          <stop offset="1" stop-color="var(--ribbon-mid)"/>
        </linearGradient>
      </defs>
      <polygon class="ribbon-tail" points="50,82 140,82 140,205 50,205 85,143" fill="var(--ribbon-dark)"/>
      <polygon class="ribbon-tail" points="1060,82 970,82 970,215 1060,215 1025,148" fill="var(--ribbon-dark)"/>
      <polygon class="ribbon-fold" points="140,152 140,200 95,152" fill="var(--ribbon-fold)"/>
      <polygon class="ribbon-fold" points="970,158 970,212 1015,158" fill="var(--ribbon-fold)"/>
      <polygon class="ribbon-band" points="135,50 983,40 983,158 135,152" fill="url(#ribbon-face)"/>
      <path class="price-panel" d="M747 736 C765 565 880 420 1100 409 L1100 736 Z" fill="var(--price-panel)"/>
    </svg>

    <h1 class="product-title">Washington State Peaches</h1>

    <p class="headline">NEW CROPS!</p>

    <ul class="benefit-list">
      <li class="benefit">
        <svg width="52" height="52" viewBox="0 0 52 52"><circle cx="26" cy="26" r="24" fill="var(--ribbon-mid)" stroke="var(--ribbon-fold)" stroke-width="3"/><path d="M14 27 L23 36 L40 15" fill="none" stroke="var(--ribbon-fold)" stroke-width="6" stroke-linecap="round" stroke-linejoin="round"/></svg>
        TREE RIPENED
      </li>
      <li class="benefit">
        <svg width="52" height="52" viewBox="0 0 52 52"><circle cx="26" cy="26" r="24" fill="var(--ribbon-mid)" stroke="var(--ribbon-fold)" stroke-width="3"/><path d="M14 27 L23 36 L40 15" fill="none" stroke="var(--ribbon-fold)" stroke-width="6" stroke-linecap="round" stroke-linejoin="round"/></svg>
        EXCELLENT FLAVOR
      </li>
    </ul>

    <div class="brand">
      <span class="brand-dot"></span>
      <p class="brand-name">Cascade Valley<br>Fruit Council</p>
    </div>

    <div class="price">
      <p class="price-amount">$9<sup>.99</sup></p>
      <p class="price-unit">per kilo</p>
    </div>
  </main>
</body>
</html>
```